CEDAR KEEP LOCKERS

Please see the attached. I need a new postcard design with a soccer theme with the headline "Score Big at Cedar Keep Lockers and make it your goal to Store Your Stuff." Everything else that is on the current card stays the same on this new card design, copy, address, phone, etc.

```html
<!DOCTYPE html>
<html lang="en">
<head>
<meta charset="utf-8">
<title>Cedar Keep Lockers – Postcard</title>
<link rel="stylesheet" href="https://fonts.googleapis.com/css2?family=Archivo+Black&family=Oswald:wght@500;700&display=swap">
<style>
  :root {
    --page: #e8e5e0;
    --red: #d81e2c;
    --ink: #1f1f1f;
    --lime: #b9de3a;
    --lime-dark: #6fae1e;
    --grass: #3f8f1c;
    --grass-light: #7cc43a;
    --yellow: #f7ec2a;
    --white: #ffffff;
  }
  * { box-sizing: border-box; margin: 0; padding: 0; }
  html, body { width: 816px; height: 1200px; overflow: hidden; }
  body { background: var(--page); position: relative; font-family: "Archivo Black", sans-serif; }

  .card { position: absolute; left: 28px; width: 760px; overflow: hidden; box-shadow: 0 4px 14px rgba(0,0,0,.25); }
  .card--front { top: 24px; height: 544px; background: radial-gradient(circle at 70% 35%, #f3fbc8 0%, var(--lime) 45%, var(--lime-dark) 100%); }
  .card--back { top: 604px; height: 572px; background: linear-gradient(160deg, #ffffff 0%, #ffffff 35%, #e4f6fb 55%, #bfe7f3 75%, var(--lime) 100%); }

  /* front */
  .headline { position: absolute; left: 30px; top: 22px; width: 450px; line-height: 1; z-index: 2; }
  .headline__lead { color: var(--red); font-size: 50px; display: block; }
  .headline__mid { color: var(--ink); font-size: 28px; display: block; margin-top: 8px; line-height: 1.12; }
  .headline__mid em { font-style: normal; color: var(--red); }
  .headline__store { color: var(--red); font-size: 56px; display: block; margin-top: 8px; }
  .headline__tail { color: var(--ink); font-size: 40px; display: block; margin-top: 2px; }
  .headline__tail em { font-style: normal; color: var(--red); }

  .ball { position: absolute; border-radius: 50%; background: radial-gradient(circle at 38% 32%, #ffffff 0%, #e9e9e9 45%, #9c9c9c 80%, #4a4a4a 100%); }
  .ball--front { left: 250px; top: 150px; width: 300px; height: 300px; }
  .grass { position: absolute; left: 0; right: 0; background: linear-gradient(180deg, var(--grass-light) 0%, var(--grass) 60%, #2a6a12 100%); }
  .grass--front { bottom: 0; height: 150px; }

  .brand-name { position: absolute; color: var(--red); font-family: "Archivo Black", sans-serif; line-height: 1.05; text-align: center; }
  .brand-name--front { right: 40px; top: 70px; width: 180px; font-size: 26px; }
  .brand-name--back { left: 40px; top: 58px; width: 160px; font-size: 22px; }

  /* back */
  .ball--back { left: -80px; top: -40px; width: 330px; height: 330px; }
  .callout { position: absolute; left: 20px; top: 252px; width: 214px; background: var(--yellow); border: 3px solid var(--red); padding: 10px 8px; text-align: center; }
  .callout__lead { font-family: "Oswald", sans-serif; font-weight: 700; color: var(--red); font-size: 17px; line-height: 1.1; text-transform: uppercase; }
  .callout__phone { color: var(--ink); font-size: 19px; margin-top: 6px; display: flex; align-items: center; justify-content: center; gap: 5px; white-space: nowrap; }
  .callout__address { font-family: "Oswald", sans-serif; font-weight: 700; color: var(--ink); font-size: 15px; margin-top: 8px; line-height: 1.2; text-transform: uppercase; }
  .callout__web { font-family: "Oswald", sans-serif; font-weight: 500; color: var(--red); font-size: 11px; margin-top: 6px; text-transform: uppercase; }

  .offer { position: absolute; left: 270px; top: 30px; width: 470px; }
  .offer__lead { color: var(--red); font-size: 40px; line-height: 1; }
  .offer__name { color: var(--red); font-size: 32px; line-height: 1.1; margin-top: 4px; white-space: nowrap; }
  .offer__today { color: var(--red); font-size: 82px; line-height: 1; margin-top: 4px; }
  .offer__list { list-style: none; margin-top: 18px; font-family: "Oswald", sans-serif; font-weight: 700; color: var(--ink); font-size: 19px; line-height: 1.3; text-transform: uppercase; }
  .offer__list li + li { margin-top: 6px; }
  .offer__list .accent { color: var(--red); }
  .offer__list s { color: var(--red); }

  .grass--back { bottom: 0; height: 78px; }
  .supplies { position: absolute; left: 0; right: 0; bottom: 24px; text-align: center; color: var(--red); font-size: 25px; white-space: nowrap; }
</style>
</head>
<body>

<section class="card card--front">
  <div class="grass grass--front" role="img" aria-label="Photo of green grass along the bottom edge"></div>
  <div class="ball ball--front" role="img" aria-label="Photo of a soccer ball resting on the grass"></div>
  <h1 class="headline">
    <span class="headline__lead">SCORE BIG AT</span>
    <span class="headline__mid">Cedar Keep Lockers and make it your <em>goal</em> to</span>
    <span class="headline__store">STORE</span>
    <span class="headline__tail">YOUR<br><em>STUFF.</em></span>
  </h1>
  <p class="brand-name brand-name--front">Cedar Keep<br>Lockers</p>
</section>

<section class="card card--back">
  <div class="ball ball--back" role="img" aria-label="Photo of a soccer ball cropped at the corner"></div>
  <p class="brand-name brand-name--back">Cedar Keep<br>Lockers</p>

  <div class="callout">
    <p class="callout__lead">Call today for<br>limited time savings!</p>
    <p class="callout__phone">
      <svg width="16" height="16" viewBox="0 0 24 24" aria-hidden="true"><path fill="#1f1f1f" d="M6.6 10.8a15.1 15.1 0 0 0 6.6 6.6l2.2-2.2a1 1 0 0 1 1-.25 11.4 11.4 0 0 0 3.6.57 1 1 0 0 1 1 1V20a1 1 0 0 1-1 1A17 17 0 0 1 3 4a1 1 0 0 1 1-1h3.5a1 1 0 0 1 1 1 11.4 11.4 0 0 0 .57 3.6 1 1 0 0 1-.25 1z"/></svg>
      (574) 555-0142
    </p>
    <p class="callout__address">1290 Larch Rd<br>Elkhart Falls, IN 46590</p>
    <p class="callout__web">www.cedarkeeplockers.com</p>
  </div>

  <div class="offer">
    <h2 class="offer__lead">SAVE BIG WITH</h2>
    <p class="offer__name">CEDAR KEEP LOCKERS</p>
    <p class="offer__today">TODAY</p>
    <ul class="offer__list">
      <li><span class="accent">5x5</span> standard-was <s>$54</s> now $47</li>
      <li><span class="accent">10x10</span> standard- was <s>$165</s> now $149</li>
      <li>Customized <span class="accent">lease &amp; payment</span> options - packing, moving &amp; storage supplies</li>
      <li><span class="accent">24 hour</span> coded gate access - motion sensor property lights</li>
      <li>Sophisticated <span class="accent">surveillance</span> - daily property inspections</li>
    </ul>
  </div>

  <div class="grass grass--back" role="img" aria-label="Photo of green grass along the bottom edge"></div>
  <p class="supplies">WE SELL LOCKS, BOXES &amp; PACKING SUPPLIES!</p>
</section>

</body>
</html>
```